Inspirational Quotes Poster Set

Braxlune is a stylish coworking space, which has a design-oriented vintage look from the 60's with an industrial touch (www.braxlune-example.com) Braxlune Quote Poster Set of 16 posters. The poster should be typo oriented and rather simple. Reflecting a bit the clean billboard design from the sixties. Minimal / simple graphical elements

Target Market(s)

Startups and Entrepreneurs

Industry/Entity Type

Startup

Font styles to use
Sans Serif

Colors

Designer to choose colors to be used in the design.

Requirements
Must have
• Posters need to be on and very stylish

```html
<!DOCTYPE html>
<html lang="en">
<head>
<meta charset="utf-8">
<title>Braxlune Quote Poster</title>
<link rel="stylesheet" href="https://fonts.googleapis.com/css2?family=Bebas+Neue&family=Open+Sans:wght@400&display=swap">
<style>
  :root {
    --paper: #fdf0e0;
    --ink: #000000;
    --navy: #173d6b;
  }
  html, body {
    margin: 0;
    padding: 0;
    overflow: hidden;
    background: var(--paper);
  }
  .poster {
    position: relative;
    width: 738px;
    height: 1200px;
    background: var(--paper);
    overflow: hidden;
  }
  .idea-icon {
    position: absolute;
    left: 265px;
    top: 95px;
    width: 220px;
    height: 230px;
  }
  .quote {
    position: absolute;
    left: 0;
    width: 738px;
    margin: 0;
    text-align: center;
    font-family: "Bebas Neue", "Oswald", sans-serif;
    font-weight: 400;
    color: var(--ink);
    line-height: 1;
    white-space: nowrap;
  }
  .quote-lead {
    top: 362px;
    left: -4px;
    font-size: 232px;
    letter-spacing: -2px;
  }
  .quote-line-1 {
    top: 604px;
    font-size: 80px;
    letter-spacing: 1px;
  }
  .quote-line-2 {
    top: 711px;
    font-size: 96px;
    letter-spacing: 1px;
  }
  .quote-line-3 {
    top: 816px;
    font-size: 96px;
    letter-spacing: 1px;
  }
  .attribution {
    position: absolute;
    left: 144px;
    top: 1031px;
    margin: 0;
    font-family: "Open Sans", "Calibri", sans-serif;
    font-size: 40px;
    line-height: 58px;
    color: var(--ink);
  }
  .attribution-role {
    display: block;
    padding-left: 24px;
  }
</style>
</head>
<body>
  <main class="poster">
    <svg class="idea-icon" viewBox="0 0 220 230" aria-hidden="true">
      <g fill="none" stroke="var(--navy)" stroke-width="15" stroke-linecap="round">
        <line x1="110" y1="10" x2="110" y2="32"/>
        <line x1="40" y1="40" x2="56" y2="56"/>
        <line x1="180" y1="40" x2="164" y2="56"/>
        <line x1="10" y1="108" x2="32" y2="108"/>
        <line x1="188" y1="108" x2="210" y2="108"/>
        <line x1="40" y1="176" x2="56" y2="160"/>
        <line x1="180" y1="176" x2="164" y2="160"/>
      </g>
      <path fill="var(--navy)" d="M110 52 C143 52 168 77 168 108 C168 126 161 138 152 148 C145 156 142 163 140 172 C138 180 133 184 126 184 L94 184 C87 184 82 180 80 172 C78 163 75 156 68 148 C59 138 52 126 52 108 C52 77 77 52 110 52 Z"/>
      <path fill="var(--navy)" d="M86 194 L134 194 C137 194 139 196 139 199 L139 206 C139 210 136 212 133 212 L131 212 C130 218 127 222 120 222 L100 222 C93 222 90 218 89 212 L87 212 C84 212 81 210 81 206 L81 199 C81 196 83 194 86 194 Z"/>
    </svg>

    <h1 class="quote quote-lead">Ideas</h1>
    <p class="quote quote-line-1">are commodity.</p>
    <p class="quote quote-line-2">Execution of</p>
    <p class="quote quote-line-3">them is not.</p>

    <p class="attribution">- Marcus Bellweather<span class="attribution-role">Corvane Chairman and CEO</span></p>
  </main>
</body>
</html>
```